Pinwheel Coffee Co. Fundraising Brochure

Our coffee company (www.pinwheelcoffee.example) is wanting to launch a fundraising option for people / schools to use. I have designed a MOCK UP but I need a real design, with the real info and good images, good layout, etc. I want to print it as an 11 x 17 and fold it twice. You can find images and the look of our material at www.pinwheelcoffee.example

Target Market(s)

School PTF
Trail Ranger troops
Moms

Industry/Entity Type

It Company

Font styles to use
Serif

Colors

Designer to choose colors to be used in the design.

Requirements
Must have
• Must mirror the look and feel of our website www.PinwheelCoffee.example

```html
<!DOCTYPE html>
<html lang="en">
<head>
<meta charset="utf-8">
<title>Pinwheel Coffee Co. Fundraising Brochure</title>
<link href="https://fonts.googleapis.com/css2?family=Arimo:wght@400;700&family=Open+Sans:wght@400;700;800&family=Oswald:wght@600;700&family=Playfair+Display+SC:wght@700&display=swap" rel="stylesheet">
<style>
:root{
  --stage:#333333;
  --paper:#ffffff;
  --ink:#2a2a2a;
  --tan:#c49a6c;
  --brick:#9b3a32;
  --brick-deep:#8a2f2a;
  --pine:#1f4d36;
  --slate:#234c6e;
  --rust-text:#b5524a;
  --pine-text:#3a7a5a;
  --slate-text:#3f6e94;
  --charcoal:#3a3a3a;
  --label:#e9dcc3;
}
*{margin:0;padding:0;box-sizing:border-box}
html,body{width:1200px;height:1000px;overflow:hidden;background:var(--stage)}
.canvas{position:relative;width:1200px;height:1000px;background:var(--stage);font-family:"Arimo",Arial,sans-serif;color:var(--ink)}
.brochure{position:absolute;left:61px;top:151px;width:1078px;height:697px;background:var(--paper);overflow:hidden}
.abs{position:absolute}
.body-copy{font-size:10.2px;line-height:14px;color:var(--ink)}
.heading{font-family:"Playfair Display SC",Georgia,serif;color:var(--tan);font-size:25px;letter-spacing:.2px;white-space:nowrap}
.roast-name{font-family:"Playfair Display SC",Georgia,serif;font-size:14px}
.rn-hearth{color:var(--rust-text)} .rn-frontier{color:var(--pine-text)} .rn-summit{color:var(--slate-text)} .rn-union{color:var(--rust-text)}
.rule{position:absolute;height:0;border-top:1.2px dashed var(--brick)}
.offer{position:absolute;left:0;width:359px;text-align:center;font-family:"Open Sans",Arial,sans-serif;color:var(--ink);white-space:nowrap}
.offer-plan{top:429px;font-size:12.5px;font-weight:800;color:var(--charcoal)}
.offer-receive{top:445px;font-size:13.5px}
.offer-free{top:458px;font-family:"Playfair Display SC",Georgia,serif;font-size:23px;color:var(--rust-text)}
.offer-list{top:486px;font-size:13.5px}
.offer-cause{top:502px;font-size:15px;font-weight:800;color:var(--charcoal)}
.bag-photo{position:absolute;left:22px;top:528px;width:88px;height:117px;background:#111;border-radius:6px 6px 3px 3px}
.badge{position:absolute;width:30px;height:30px;border-radius:50%;background:var(--brick-deep);color:#fff;font-family:"Oswald",Arial,sans-serif;font-weight:700;font-size:13px;line-height:30px;text-align:center}
.plan-caption{position:absolute;font-size:8.5px;text-align:center;width:110px;color:var(--ink)}
.plan-caption b{display:block;font-weight:700}
.band{position:absolute;left:359px;width:359px}
.band-hearth{top:0;height:180px;background:var(--brick)}
.band-frontier{top:180px;height:178px;background:var(--pine)}
.band-summit{top:358px;height:176px;background:var(--slate)}
.band-union{top:534px;height:163px;background:var(--brick)}
.product-card{position:absolute;background:#fff;border-radius:9px;padding:7px}
.product-photo{width:100%;height:100%;border-radius:4px}
.photo-hearth{background:linear-gradient(160deg,#a3453b 0 40%,var(--label) 40% 100%)}
.photo-frontier{background:linear-gradient(160deg,#2a5a40 0 38%,var(--label) 38% 100%)}
.photo-summit{background:linear-gradient(160deg,#2d587a 0 38%,var(--label) 38% 100%)}
.photo-union{background:linear-gradient(160deg,var(--label) 0 30%,#a3453b 30% 46%,var(--label) 46% 100%)}
.brand{position:absolute;width:140px;text-align:center}
.brand-mark{display:block;margin:0 auto 3px;width:26px;height:26px;border-radius:50%;border:2px solid #fff}
.brand-name{font-family:"Arimo",Arial,sans-serif;font-weight:700;color:#fff;font-size:17px;letter-spacing:.6px;line-height:19px}
.brand-roast{font-family:"Arimo",Arial,sans-serif;font-weight:700;color:#2b2b2b;font-size:13px;letter-spacing:.5px;line-height:16px}
.band-copy{position:absolute;color:#fff;font-size:8.6px;line-height:11.6px;text-align:justify}
.story{position:absolute;left:739px;top:42px;font-size:10.4px;line-height:14.6px;color:var(--ink);white-space:nowrap}
.story p{margin-bottom:13px}
.inbox-banner{position:absolute;left:756px;top:380px;width:286px;height:30px;background:var(--brick-deep);color:#fff;font-family:"Oswald",Arial,sans-serif;font-weight:700;font-size:22px;line-height:30px;text-align:center;letter-spacing:.4px}
.center-col{position:absolute;left:739px;width:320px;text-align:center}
.inbox-copy{top:413px;font-size:13.5px;line-height:16.5px;color:#222}
.signup{top:474px;font-family:"Oswald",Arial,sans-serif;font-weight:700;color:var(--brick-deep);font-size:25px}
.signup small{font-family:"Arimo",Arial,sans-serif;font-weight:400;font-size:14px;color:#222}
.signup-url{top:511px;font-family:"Open Sans",Arial,sans-serif;font-weight:700;font-size:14px;color:var(--brick-deep)}
.touch-lead{top:557px;font-size:16px;color:#222}
.touch-head{top:573px;font-family:"Oswald",Arial,sans-serif;font-weight:700;color:var(--brick-deep);font-size:26px;letter-spacing:.3px}
.social{position:absolute;left:831px;top:622px;display:flex;gap:6px}
.social span{width:29px;height:29px;border-radius:50%;background:var(--brick-deep);display:block}
</style>
</head>
<body>
<div class="canvas">
  <div class="brochure">

    <!-- Left panel: roast guide and subscription offer -->
    <h1 class="abs heading" style="left:18px;top:26px">What Roast Do I Want?</h1>

    <p class="abs body-copy" style="left:19px;top:84px;width:322px">Pinwheel's Hearthside Roast pairs well with pastries and lighter desserts. With bright acids, it's lively yet never overpowering, with a smooth clean finish. Whether you're starting the day off on your back porch step or hosting your guests after dinner, our warm and welcoming <span class="roast-name rn-hearth">Hearthside Roast</span> fits the bill.</p>

    <p class="abs body-copy" style="left:19px;top:170px;width:322px">A gentle earthiness and sturdy mouthfeel make Frontier roast a very satisfying single cup choice. If you can only have one cup of coffee a day, make it a cup of <span class="roast-name rn-frontier">Frontier Roast.</span> Its full body pairs well with savory and sweet treats.</p>

    <p class="abs body-copy" style="left:19px;top:243px;width:322px">Bold and energetic, our dark <span class="roast-name rn-summit">Summit Roast</span> cannot be overlooked. The deep, rich flavor pairs well with mid-afternoon snacks and late-night conversations. Our Summit Roast has flavor notes of dark chocolate and cocoa with hints of cherry and plum.</p>

    <p class="abs body-copy" style="left:19px;top:329px;width:322px">A spirited mix of dark and medium-dark roasts to start your day off with a spark- the same way great stories begin! A combination of African and Central American beans, the <span class="roast-name rn-union">Union Blend</span> celebrates the shared table that brings friends and neighbors together.</p>

    <div class="rule" style="left:19px;top:416px;width:321px"></div>

    <p class="offer offer-plan">SUBSCRIBE TO A 2 OR 4 WEEK PLAN</p>
    <p class="offer offer-receive">&amp; receive a</p>
    <p class="offer offer-free">FREE French Press</p>
    <p class="offer offer-list">with your list order!</p>
    <p class="offer offer-cause">CAUSE RECEIVES 22%!</p>

    <div class="bag-photo" role="img" aria-label="Black Pinwheel Coffee Co. bag of beans"></div>
    <div class="badge" style="left:77px;top:522px">$25</div>
    <p class="plan-caption" style="left:10px;top:650px">Individual Bag(s) Once<b>CAUSE RECEIVES 18%</b></p>

    <svg class="abs" style="left:140px;top:565px" width="78" height="75" viewBox="0 0 78 75" aria-label="Two week plan calendar">
      <rect x="1" y="1" width="76" height="73" fill="#fff" stroke="#111" stroke-width="2"/>
      <rect x="3" y="3" width="72" height="12" fill="#111"/>
      <g fill="#9b3a32">
        <rect x="3" y="17" width="72" height="12"/><rect x="3" y="31" width="72" height="12"/>
        <rect x="3" y="45" width="72" height="12"/><rect x="3" y="59" width="40" height="12"/>
      </g>
      <g stroke="#fff" stroke-width="1.6">
        <line x1="13.5" y1="3" x2="13.5" y2="72"/><line x1="24" y1="3" x2="24" y2="72"/><line x1="34.5" y1="3" x2="34.5" y2="72"/>
        <line x1="45" y1="3" x2="45" y2="72"/><line x1="55.5" y1="3" x2="55.5" y2="72"/><line x1="66" y1="3" x2="66" y2="72"/>
        <line x1="3" y1="16" x2="75" y2="16"/><line x1="3" y1="30" x2="75" y2="30"/><line x1="3" y1="44" x2="75" y2="44"/><line x1="3" y1="58" x2="75" y2="58"/>
      </g>
    </svg>
    <div class="badge" style="left:193px;top:548px">$22</div>
    <p class="plan-caption" style="left:123px;top:643px">2 Week Plan</p>

    <svg class="abs" style="left:242px;top:565px" width="78" height="75" viewBox="0 0 78 75" aria-label="Four week plan calendar">
      <rect x="1" y="1" width="76" height="73" fill="#fff" stroke="#111" stroke-width="2"/>
      <g fill="#9b3a32">
        <rect x="3" y="17" width="72" height="12"/><rect x="3" y="31" width="72" height="12"/>
        <rect x="3" y="45" width="72" height="12"/><rect x="3" y="59" width="72" height="12"/>
      </g>
      <g stroke="#111" stroke-width="1.2">
        <line x1="13.5" y1="3" x2="13.5" y2="72"/><line x1="24" y1="3" x2="24" y2="72"/><line x1="34.5" y1="3" x2="34.5" y2="72"/>
        <line x1="45" y1="3" x2="45" y2="72"/><line x1="55.5" y1="3" x2="55.5" y2="72"/><line x1="66" y1="3" x2="66" y2="72"/>
        <line x1="3" y1="16" x2="75" y2="16"/><line x1="3" y1="30" x2="75" y2="30"/><line x1="3" y1="44" x2="75" y2="44"/><line x1="3" y1="58" x2="75" y2="58"/>
      </g>
    </svg>
    <div class="badge" style="left:294px;top:548px">$23</div>
    <p class="plan-caption" style="left:226px;top:643px">4 Week Plan</p>

    <!-- Middle panel: roast bands -->
    <div class="band band-hearth"></div>
    <div class="band band-frontier"></div>
    <div class="band band-summit"></div>
    <div class="band band-union"></div>
    <svg class="abs" style="left:359px;top:0" width="359" height="697" viewBox="0 0 359 697" aria-hidden="true">
      <path d="M160 180 Q176 180 180 206 Q184 180 200 180 Z" fill="#9b3a32"/>
      <path d="M160 358 Q176 358 180 332 Q184 358 200 358 Z" fill="#234c6e"/>
      <path d="M160 534 Q176 534 180 508 Q184 534 200 534 Z" fill="#9b3a32"/>
    </svg>

    <div class="product-card" style="left:379px;top:30px;width:128px;height:123px">
      <div class="product-photo photo-hearth" role="img" aria-label="Hearthside coffee bag with beans and a pastry"></div>
    </div>
    <div class="brand" style="left:591px;top:30px">
      <span class="brand-mark"></span>
      <div class="brand-name">PINWHEEL</div>
      <div class="brand-roast">HEARTHSIDE</div>
    </div>
    <p class="band-copy" style="left:539px;top:99px;width:166px">This bright, medium-roasted coffee has a taste that's steady, cup after cup, from breakfast to dinner. Hearthside's medium darkness draws out the natural oils in our single origin beans without roasting away their distinct flavors.</p>

    <div class="brand" style="left:345px;top:203px">
      <span class="brand-mark"></span>
      <div class="brand-name">PINWHEEL</div>
      <div class="brand-roast">FRONTIER</div>
    </div>
    <p class="band-copy" style="left:378px;top:277px;width:155px">The balance and steadiness of Frontier comes from the Latin American hills where the beans were grown and picked, but the weight and the boldness are given by the medium-dark roast. Hearty, rugged, and (slightly) wild.</p>
    <div class="product-card" style="left:571px;top:201px;width:129px;height:148px">
      <div class="product-photo photo-frontier" role="img" aria-label="Frontier coffee bag with beans and cookies"></div>
    </div>

    <div class="product-card" style="left:379px;top:377px;width:128px;height:140px">
      <div class="product-photo photo-summit" role="img" aria-label="Summit coffee bag with beans and pretzels"></div>
    </div>
    <div class="brand" style="left:591px;top:380px">
      <span class="brand-mark"></span>
      <div class="brand-name">PINWHEEL</div>
      <div class="brand-roast">SUMMIT</div>
    </div>
    <p class="band-copy" style="left:533px;top:452px;width:172px">Summit is a bold take on a sturdy African single origin coffee. Glossy and dark-roasted, this coffee stands well on its own. If you are looking for a bit more drive to power through your afternoon, Summit is for you.</p>

    <div class="brand" style="left:345px;top:546px">
      <span class="brand-mark"></span>
      <div class="brand-name">PINWHEEL</div>
      <div class="brand-roast" style="font-size:11px">UNION BLEND</div>
    </div>
    <p class="band-copy" style="left:378px;top:612px;width:155px">A spirited mix of dark and medium-dark roasts to start your day off with a spark- the same way great stories begin! Our motto for this blend? Ex Multis Granis - out of many beans, one fantastic coffee!</p>
    <div class="product-card" style="left:569px;top:544px;width:131px;height:141px">
      <div class="product-photo photo-union" role="img" aria-label="Union Blend coffee bag with beans and a breakfast plate"></div>
    </div>

    <!-- Right panel: story and newsletter -->
    <div class="story">
      <p>Pinwheel Coffee began the way many good ideas do; as a pastime.<br>A few friends at the office were fed up with stale coffee.<br>Tasting freshly roasted beans showed them it was far<br>better than anything sold in nearby grocery stores and<br>coffee bars. So we started &nbsp;testing home roasters,<br>all kinds of green beans, burr grinders, and pour-over cones.<br>We sharpened our choice of beans and our roasting methods,<br>and in 2014, opened the Pinwheel Coffee Company to bring<br>our small batch craft coffee to everyone.</p>
      <p>Here at Pinwheel, we never roast until you order.<br>We don't keep storerooms stacked with pre-roasted, pre-bagged beans<br>going flat while they wait on a buyer. Once your order arrives,<br>we roast your beans, hand stamp each bag with the date-<br>and send them out right away so you'll always have a freshly<br>roasted cup ready.</p>
      <p>Another thing we love about Pinwheel Coffee is that every bag<br>holds a true 16-ounce pound. Many roasters begin with<br>16 ounces of green beans, but after roasting, only 12 ounces remain.<br>We believe a pound should be a pound, so we plan for that in the<br>roasting process to give you more bean for your money.</p>
    </div>

    <div class="rule" style="left:737px;top:364px;width:322px"></div>
    <div class="inbox-banner">KEEP YOUR INBOX FRESH</div>
    <p class="center-col inbox-copy">Get Brewnotes delivered fresh to your inbox.<br>Brewing and food pairing tips, recipes and<br>special offers.</p>
    <p class="center-col signup">SIGN UP NOW <small>at</small></p>
    <p class="center-col signup-url">www.PinwheelCoffee.example/news</p>
    <div class="rule" style="left:737px;top:542px;width:322px"></div>
    <p class="center-col touch-lead">Now that we know each other,</p>
    <p class="center-col touch-head">LETS STAY IN TOUCH.</p>
    <div class="social" aria-label="Social and email links">
      <span></span><span></span><span></span>
      <svg width="29" height="29" viewBox="0 0 29 29" aria-label="Email">
        <circle cx="14.5" cy="14.5" r="14.5" fill="#8a2f2a"/>
        <rect x="7" y="9.5" width="15" height="10" fill="none" stroke="#fff" stroke-width="1.6"/>
        <path d="M7 9.5 L14.5 15.5 L22 9.5" fill="none" stroke="#fff" stroke-width="1.6"/>
      </svg>
    </div>

  </div>
</div>
</body>
</html>
```